依頼詳細
会社の封筒デザインを新しくしたいと考えています。
シンプルでありながらも洗練された高級感のあるデザインを希望します。
建築にとらわれない新しいデザインをお願いします。

封筒デザイン3種です。
ペトモア
長3封筒窓無し 表フルカラー 全面印刷
角2封筒窓無し 表フルカラー 全面印刷 縦・横

ペトモアへ印刷発注予定の為、専用テンプレートを使用し、そのままペトモアで印刷依頼が可能な仕様のデータで納品下さい。
記載項目
会社ロゴ
郵便番号、住所、電話番号、FAX番号、URL
希望イメージ
シンプル 複雑
単色 カラフル
暗い 明るい
日常 高級
遊び心 厳粛
未来的 伝統的
女性的 男性的
希望する色
青系、水色系、無彩色系
納品ファイル
• 高解像度JPG (.jpg)
• イラストレーター形式 (.ai)
• PNG形式 (.png)
補足説明
現在使用しているデザインのPDFを添付します。
現在の封筒デザインが添付出来ていなかった為再度添付させていただきます。
■ 選んだ理由

シンプルかつ今までとは雰囲気の違うデザインが気に入り選定させていただきました。

■ 提案者全員のお礼・コメント

このたびは多数の御提案ありがとうございました。
今後また機会がございましたらよろしくお願いいたします。

```html
<!DOCTYPE html>
<html lang="ja">
<head>
<meta charset="utf-8">
<title>Veltor 角2封筒</title>
<link href="https://fonts.googleapis.com/css2?family=Noto+Sans+JP:wght@400;500;700;900&display=swap" rel="stylesheet">
<style>
  :root {
    --paper: #ffffff;
    --ink: #2b2b2b;
    --ink-soft: #555555;
    --rule: #9a9a9a;
    --fold: #e6e6e6;
    --band-dark: #6e6e6e;
    --band-mid: #b4b4b4;
    --band-light: #f2f2f2;
    --mark-light: #d8d8d8;
    --mark-dark: #5e5e5e;
  }
  html, body {
    margin: 0;
    padding: 0;
    width: 829px;
    height: 1200px;
    overflow: hidden;
    background: var(--paper);
  }
  .envelope {
    position: relative;
    width: 829px;
    height: 1200px;
    overflow: hidden;
    background: var(--paper);
    font-family: "Noto Sans JP", sans-serif;
    color: var(--ink);
  }
  .tone-band {
    position: absolute;
    left: 0;
    top: 440px;
    width: 100%;
    height: 380px;
    background:
      linear-gradient(90deg, var(--band-dark) 0%, rgba(180,180,180,0.55) 22%, rgba(255,255,255,0) 50%, rgba(180,180,180,0.55) 78%, var(--band-dark) 100%),
      linear-gradient(180deg, var(--paper) 0%, var(--band-light) 30%, var(--band-mid) 60%, var(--band-light) 85%, var(--paper) 100%);
    -webkit-mask-image: linear-gradient(180deg, transparent 0%, #000 30%, #000 70%, transparent 100%);
    mask-image: linear-gradient(180deg, transparent 0%, #000 30%, #000 70%, transparent 100%);
  }
  .flap-fold {
    position: absolute;
    left: 0;
    top: 150px;
    width: 100%;
    border-top: 1px solid var(--fold);
  }
  .flap-brand {
    position: absolute;
    top: 56px;
    right: 88px;
    transform: rotate(180deg);
    display: flex;
    align-items: center;
    gap: 14px;
  }
  .flap-brand .brand-dot { width: 34px; height: 34px; }
  .brand-name {
    font-weight: 900;
    letter-spacing: 0.02em;
    color: var(--ink);
    line-height: 1;
  }
  .flap-brand .brand-name { font-size: 44px; }

  .center-brand {
    position: absolute;
    left: 0;
    right: 0;
    top: 690px;
    display: flex;
    flex-direction: column;
    align-items: center;
    gap: 20px;
  }
  .center-brand .brand-dot { width: 150px; height: 150px; }
  .center-brand .brand-name { font-size: 64px; }

  .sender {
    position: absolute;
    left: 488px;
    top: 990px;
    width: 320px;
    font-size: 12px;
    line-height: 1.75;
    color: var(--ink);
  }
  .sender .company {
    display: flex;
    align-items: baseline;
    gap: 6px;
    font-size: 13px;
    margin-bottom: 6px;
  }
  .sender .company .brand-name { font-size: 30px; }
  .sender .company .kana { font-size: 12px; }
  .sender .line { font-weight: 500; }
  .sender .line.bold { font-weight: 700; }

  .enclosure {
    position: absolute;
    left: 160px;
    top: 1046px;
    font-size: 12px;
    line-height: 1.9;
    color: var(--ink-soft);
  }
  .enclosure .item { display: flex; align-items: center; gap: 8px; }
  .enclosure .box {
    width: 11px;
    height: 11px;
    border: 1px solid var(--ink-soft);
    box-sizing: border-box;
  }
  .enclosure-blank {
    position: absolute;
    left: 290px;
    top: 1064px;
    width: 180px;
    border-bottom: 1px solid var(--rule);
    text-align: right;
    font-size: 12px;
    color: var(--ink-soft);
    padding-bottom: 2px;
  }
</style>
</head>
<body>
<main class="envelope">
  <div class="tone-band" aria-hidden="true"></div>

  <div class="flap-brand">
    <svg class="brand-dot" viewBox="0 0 34 34" aria-hidden="true">
      <circle cx="17" cy="17" r="17" fill="var(--mark-dark)"/>
    </svg>
    <span class="brand-name">Veltor</span>
  </div>
  <div class="flap-fold"></div>

  <section class="center-brand">
    <svg class="brand-dot" viewBox="0 0 150 150" aria-hidden="true">
      <defs>
        <linearGradient id="dotShade" x1="0" y1="0" x2="0" y2="1">
          <stop offset="0" stop-color="var(--mark-light)"/>
          <stop offset="1" stop-color="var(--mark-dark)"/>
        </linearGradient>
      </defs>
      <circle cx="75" cy="75" r="75" fill="url(#dotShade)"/>
    </svg>
    <span class="brand-name">Veltor</span>
  </section>

  <section class="sender">
    <div class="company">
      <span>株式会社</span>
      <span class="brand-name">Veltor</span>
      <span class="kana">（ヴェルター）</span>
    </div>
    <div class="line">〒123-0045　東京都港南区若葉町120-3</div>
    <div class="line bold">TEL.00-0000-0000 FAX.00-0000-0000</div>
    <div class="line">ホームページ：info@veltor-example.com</div>
  </section>

  <section class="enclosure">
    <div class="item"><span class="box"></span>請求書在中</div>
    <div class="item"><span class="box"></span>納品書在中</div>
  </section>
  <div class="enclosure-blank">在中</div>
</main>
</body>
</html>
```